Food Safety 1-California workers only

3.25" by 4.5" Black and White Magazine Ad
This ad is to train California workers only.
Workers will be trained on: Food Safety, FSMA (Food Safety Modernization Act), using equipment safety, food processing production skills, worker safety, supervisory skills, communication skills.
"FREE TRAINING", The company does the training or Keystone Learning will provide the training.
Training grants range from $100,000 to $400,000.
Companies must be in business for profit.
Companies must train 200 employees or more.
This program is for California workers only.
Incumbent or new-hires are eligible.

Target Market(s)

California food processors, farms, food packaging, food processors, companies under FSMA, food safety, food production who need to train employees.

Industry/Entity Type

Food Production

Font styles to use
Serif
Sans Serif

Colors

Designer to choose colors to be used in the design.

Requirements
Must have
• This is a 3.25 inch by 4.5 inch magazine ad. It must be black and white. No color.
• The deliverable must be in basic PhotoShop. The ad does not need to include any graphics and be text only if needed. If you have a black and white graphic that will show well.
• Look at www.KLGFoodSafety..com
• Use the text from "MEALBOX-Photoshop-052018" file as your starting point.
Nice to have
• A black and white graphic about food. See www.KLGFoodSafety.com
Should not have
• No color.

```html
<!DOCTYPE html>
<html lang="en">
<head>
<meta charset="utf-8">
<title>Free Training Ad</title>
<link href="https://fonts.googleapis.com/css2?family=Anton&family=Archivo+Black&family=Lato:wght@700&family=Playfair+Display:wght@700&family=Libre+Baskerville&display=swap" rel="stylesheet">
<style>
  :root {
    --ink: #0a0a0a;
    --paper: #f7f7f7;
    --backdrop: #c9cad9;
    --reverse: #ffffff;
  }
  * { box-sizing: border-box; margin: 0; padding: 0; }
  html, body { width: 1200px; height: 946px; overflow: hidden; background: var(--backdrop); }
  .ad {
    position: absolute; left: 280px; top: 30px;
    width: 640px; height: 886px;
    background: var(--paper); overflow: hidden; color: var(--ink);
  }
  .ad__panel { position: absolute; inset: 0; }
  .headline {
    position: absolute; left: 0; right: 0; top: 14px;
    font-family: "Anton", "Archivo Black", sans-serif;
    font-size: 120px; line-height: 1; text-align: center; letter-spacing: 1px;
  }
  .topics {
    position: absolute; left: 20px; right: 20px; top: 150px; height: 38px;
    background: var(--ink); color: var(--reverse);
    font-family: "Archivo Black", sans-serif; font-size: 17px;
    display: flex; align-items: center; justify-content: center; letter-spacing: .3px;
  }
  .slogan {
    position: absolute; left: 0; right: 0; top: 200px;
    font-family: "Anton", sans-serif; font-size: 58px; line-height: 1.05;
    text-align: center; text-transform: uppercase;
  }
  .qualify {
    position: absolute; left: 60px; top: 418px; color: var(--reverse);
  }
  .qualify__title {
    font-family: "Playfair Display", serif; font-size: 30px; margin-bottom: 10px;
  }
  .qualify__list { list-style: none; font-family: "Libre Baskerville", serif; font-size: 20px; line-height: 30px; }
  .qualify__list li::before { content: "• "; }
  .contact-tab {
    position: absolute; left: 330px; top: 690px; width: 190px; height: 44px;
    background: var(--ink); color: var(--reverse);
    font-family: "Lato", sans-serif; font-size: 26px;
    display: flex; align-items: center; justify-content: center; letter-spacing: 1px;
  }
  .contact-web {
    position: absolute; left: 380px; top: 742px;
    font-family: "Lato", sans-serif; font-size: 19px; line-height: 28px;
  }
  .contact-office {
    position: absolute; left: 40px; top: 770px;
    font-family: "Lato", sans-serif; font-size: 22px; line-height: 27px;
  }
</style>
</head>
<body>
  <article class="ad">
    <svg class="ad__panel" width="640" height="886" viewBox="0 0 640 886" aria-hidden="true">
      <path d="M0 392 Q320 300 640 338 L640 660 Q420 690 0 770 Z" fill="#0a0a0a"/>
    </svg>
    <h1 class="headline">FREE TRAINING</h1>
    <p class="topics">FOOD SAFETY (FSMA) PRODUCTION SKILLS WORKER SAFETY</p>
    <p class="slogan">“We do the training and<br>the state pays for it!”</p>
    <section class="qualify">
      <h2 class="qualify__title">How to Qualify:</h2>
      <ul class="qualify__list">
        <li>Train California Workers Only</li>
        <li>Trainees must earn $11/hour</li>
        <li>Full-time workers only</li>
        <li>Employees must attend at least 8 Hours of training</li>
        <li>You must train 200 or more employees</li>
        <li>Incumbent or New-Hire workers are eligible</li>
        <li>Seasonal workers are eligibl</li>
      </ul>
    </section>
    <p class="contact-tab">CONTACT:</p>
    <address class="contact-web" style="font-style:normal">
      www.KLGCAL.com<br>
      www.KLGFoodSafety.com<br>
      Dan.Harper@KLGCAL.com<br>
      Phone: (949) 555-0142
    </address>
    <address class="contact-office" style="font-style:normal">
      Daniel Harper<br>
      Keystone Learning Company, Inc.<br>
      1850 Alder Crest Way,<br>
      Suite 310, Irvine, CA 92604
    </address>
  </article>
</body>
</html>
```